Flyer Design Project

I am opening a yoga studio called Willowmere Yoga .Pilates. Fitness
and require a flyer that will be letterbox dropped. It will two sided - DL size.100mm × 210mm

The studio will offer Vinyasa Flow Yoga and Mat Pilates classes. We aim to enable people to lead healthier, happier lives through improved strength, flexibility and general well being that regular yoga and pilates practice offers.

We offer group classes, private and semi private sessions in yoga and pilates.

it must have the logo on it- I have uploaded the logo in two versions - not sure what will look the best.

pick up one of the colours from the logo as the background colour.

Side one:
Simple and clean with one side showing logo and address details, website and with simple intro about studio (if it fits)

Location: 1st Floor, 17 Larkspur Parade, Tindale, 3286
phone: 0428 596143
www.willowmeretindale.com.au

OPENING OCTOBER

other side - class descriptions and intro offer for new clients
$20 for 7 days of classes
$99 for 1 month unlimited.

Class descriptions:
Vinyasa Flow yoga: A class that flows from pose to pose integrating breath, alignment, strength and power. All levels are catered for in a warm room heated to around 26 degrees. You will leave feeling inspired, empowered and energised.

Mat Pilates: A strong, challenging class integrating the key principles of pilates: concentration, control, centring, precision, flowing movement and breath. Using the core as a focus to develop these principles you will be hooked on the physical freedom you experience post workout:improved strength, flexibility and vitality that pilates offers.

Private and semi Private tuition available.

Target Market(s)

mainly women, athletic, 35-55 age, middle class, well educated

Industry/Entity Type

Fitness

Requirements
Must have
• 2 pages
the logo

Should not have
• no pics

```html
<!DOCTYPE html>
<html lang="en">
<head>
<meta charset="utf-8">
<title>Willowmere Yoga – DL Flyer</title>
<link rel="stylesheet" href="https://fonts.googleapis.com/css2?family=Arimo:ital,wght@0,400;0,700;1,700&display=swap">
<style>
  :root {
    --stage: #2c2d31;
    --paper: #ffffff;
    --slate: #5e5e60;
    --slate-dark: #4c4c4e;
    --ink: #1e1e1e;
    --white: #ffffff;
    --gold: #ffd21f;
    --amber: #f4a21a;
    --bronze: #8a6d4a;
    --photo-warm: #c9a98a;
    --photo-deck: #8e7a66;
    --photo-skin: #e6c2a2;
    --photo-top: #5f88b8;
    --accent-red: #d8232a;
  }
  * { box-sizing: border-box; margin: 0; padding: 0; }
  html, body { width: 1200px; height: 638px; overflow: hidden; }
  body {
    background: var(--stage);
    font-family: "Arimo", Arial, sans-serif;
    position: relative;
  }
  .flyer-side {
    position: absolute;
    top: 39px;
    width: 267px;
    height: 560px;
    overflow: hidden;
  }
  .flyer-front { left: 327px; background: var(--paper); }
  .flyer-back  { left: 606px; background: var(--slate); }

  /* Front */
  .front-photo {
    position: absolute; left: 0; top: 0; width: 100%; height: 224px;
    background: linear-gradient(180deg, #d9d2c6 0%, var(--photo-warm) 45%, var(--photo-deck) 100%);
  }
  .front-divider {
    position: absolute; left: 0; top: 224px; width: 100%; height: 14px;
    background: linear-gradient(180deg, #efe7dc, #d6c7b2);
    border-bottom: 1px solid var(--bronze);
  }
  .opening-banner {
    position: absolute; left: 40px; top: 274px; width: 187px; height: 34px;
    border: 2px solid var(--bronze);
    background: linear-gradient(90deg, var(--amber), var(--gold));
    display: flex; align-items: center; justify-content: center;
    font-weight: 700; font-size: 16px; color: var(--ink); letter-spacing: 0.2px;
  }
  .contact-block {
    position: absolute; left: 0; top: 332px; width: 100%;
    text-align: center; color: var(--ink);
  }
  .contact-phone { font-weight: 700; font-style: italic; font-size: 15px; }
  .contact-web { font-weight: 700; font-size: 10.5px; margin-top: 9px; }
  .contact-address { font-size: 16px; line-height: 1.25; margin-top: 12px; }
  .brand-lockup {
    position: absolute; left: 0; top: 472px; width: 100%;
    display: flex; flex-direction: column; align-items: center; gap: 8px;
  }
  .brand-dot {
    width: 50px; height: 50px; border-radius: 50%;
    background: var(--gold);
  }
  .brand-name {
    font-weight: 700; font-size: 12.5px; color: var(--slate-dark);
    letter-spacing: 0.3px;
  }

  /* Back */
  .back-photo {
    position: absolute; left: 0; top: 0; width: 100%; height: 189px;
    background: linear-gradient(160deg, var(--photo-skin) 0%, #f2e6da 40%, var(--photo-top) 75%, #e9e5e2 100%);
  }
  .back-caption {
    position: absolute; left: 0; top: 189px; width: 100%; height: 19px;
    background: var(--slate-dark);
    color: var(--white); font-size: 10px; text-align: center; line-height: 19px;
  }
  .offer-pill {
    position: absolute; left: 18px; top: 232px; width: 231px; height: 46px;
    border-radius: 12px; border: 3px solid var(--amber);
    background: linear-gradient(180deg, #fff06a, var(--gold) 55%, #f7b81b);
    display: flex; flex-direction: column; justify-content: center; align-items: center;
    font-weight: 700; font-size: 11px; color: var(--ink); line-height: 1.35;
  }
  .class-list {
    position: absolute; left: 12px; top: 296px; width: 243px;
    color: var(--white);
  }
  .class-list h2 { font-size: 13.5px; font-weight: 700; margin-bottom: 5px; }
  .class-list p {
    font-size: 10.4px; line-height: 1.3; text-align: justify; margin-bottom: 9px;
  }
  .class-list strong { font-weight: 700; }
  .tuition-note {
    position: absolute; left: 12px; top: 531px; width: 243px;
    color: var(--white); font-weight: 700; font-size: 11.2px;
  }
</style>
</head>
<body>
  <section class="flyer-side flyer-front">
    <div class="front-photo" role="img" aria-label="Photo of two women holding a low lunge yoga pose on mats on a timber deck"></div>
    <div class="front-divider"></div>
    <div class="opening-banner">OPENING OCTOBER</div>
    <div class="contact-block">
      <p class="contact-phone">Contact Us 0428 596143</p>
      <p class="contact-web">Log On : www.willowmeretindale.com.au</p>
      <p class="contact-address">1st Floor, 17 Larkspur Parade,<br>Tindale, 3286</p>
    </div>
    <div class="brand-lockup">
      <span class="brand-dot"></span>
      <span class="brand-name">Willowmere Yoga .Pilates. Fitness</span>
    </div>
  </section>

  <section class="flyer-side flyer-back">
    <div class="back-photo" role="img" aria-label="Close photo of a woman's torso in a blue top with hands in prayer position"></div>
    <div class="back-caption">Class Descriptions And Intro Offer For New Clients</div>
    <div class="offer-pill">
      <span>$20 for 7 days of classes</span>
      <span>$99 for 1 month unlimited.</span>
    </div>
    <div class="class-list">
      <h2>CLASS DESCRIPTIONS</h2>
      <p><strong>Vinyasa Flow yoga :</strong> A class that flows from pose to pose integrating breath, alignment, strength and power. All levels are catered for in a warm room heated to around 26 degrees. You will leave feeling inspired, empowered and energised.</p>
      <p><strong>Mat Pilates :</strong> A strong, challenging class integrating the key principles of pilates: concentration, control, centring, precision, flowing movement and breath. Using the core as a focus to develop these principles you will be hooked on the physical freedom you experience post workout:improved strength, flexibility and vitality that pilates offers.</p>
    </div>
    <p class="tuition-note">Private and semi Private tuition available</p>
  </section>
</body>
</html>
```